Web Design for UK Based Technology Company*

Norvexa is a new entrant in the data marketplace.
It is offering two direct API services to help clients access:
- Company Data
- Location Data
We also offer data services and consulting to help companies to integrate our API services and the data derived from them into their businesses. Our aim is to offer both the technology and services to help businesses use and integrate data better. It is a modern business built to support a modern world.

Target Market(s)

Business Professionals and decision makers

Industry/Entity Type

It Service

Number of Pages Required

5+ page

Font styles to use
Sans Serif

Colors

Designer to choose colors to be used in the design.

Requirements
Must have
• The full suite of PSD designs taking into account the layouts and wireframes supplied with which it will be compared. Focus on the homepage first. It has to have a consistent theme/feel. It has to fit with the logo.
Nice to have
• Simple, clean, a few strong ideas.
Should not have
• Cartoons, overdesign, loud colours.

```html
<!DOCTYPE html>
<html lang="en">
<head>
<meta charset="utf-8">
<title>Norvexa – Company and Location Data</title>
<link href="https://fonts.googleapis.com/css2?family=Lato:wght@400;700;900&family=Open+Sans:wght@400;600&display=swap" rel="stylesheet">
<style>
:root{
  --navy:#163a63;
  --navy-deep:#0d1b30;
  --blue:#1ba3dd;
  --blue-dark:#1474b8;
  --ink:#222;
  --text:#555;
  --muted:#777;
  --line:#e3e3e3;
  --white:#fff;
}
*{box-sizing:border-box;margin:0;padding:0}
html,body{width:1200px;height:4511px;overflow:hidden}
body{position:relative;background:var(--white);font-family:"Open Sans",Arial,sans-serif;color:var(--text)}
.abs{position:absolute}
.btn{position:absolute;display:flex;align-items:center;justify-content:center;border:2px solid var(--blue);color:var(--blue);font:700 15px "Lato",sans-serif;letter-spacing:.3px;background:var(--white)}
.btn.light{border-color:var(--white);color:var(--white);background:transparent}
/* header */
.brand{left:110px;top:22px;display:flex;align-items:center;gap:12px;font:700 40px "Lato",sans-serif;color:var(--navy)}
.brand .mark{width:26px;height:26px;background:var(--navy)}
.toplinks{left:614px;top:24px;font:400 14px "Lato",sans-serif;color:#444;display:flex;gap:10px;align-items:center}
.toplinks svg{width:12px;height:12px;fill:var(--blue);vertical-align:-1px;margin-right:4px}
.toplinks .sep{color:#999}
.trial-top{left:970px;top:16px;width:118px;height:40px;background:var(--blue);color:var(--white);font:700 14px "Lato",sans-serif;display:flex;align-items:center;justify-content:center}
.nav{left:574px;top:74px;display:flex;gap:35px;font:700 15px "Lato",sans-serif;color:#222}
/* hero */
.hero{left:0;top:114px;width:1200px;height:529px;background:radial-gradient(ellipse at 30% 20%,#1d3a63 0%,#0d1b30 55%,#0a1424 100%)}
.hero-panel{left:110px;top:254px;width:976px;height:223px;background:rgba(27,120,180,.78)}
.hero-split{left:0;top:114px}
.hero-title{color:var(--white);font:700 30px/43px "Lato",sans-serif}
.hero-circle{left:501px;top:256px;width:200px;height:200px;border-radius:50%;background:var(--white);border:9px solid #d8dde3;display:flex;align-items:center;justify-content:center;text-align:center;font:700 23px/34px "Lato",sans-serif;color:var(--ink)}
/* intro */
.intro{left:190px;top:722px;width:820px;text-align:center;font-size:15px;line-height:32.6px;color:#555}
.intro p+p{margin-top:32.6px}
/* products */
.photo{position:absolute}
.card{position:absolute;background:var(--white);box-shadow:0 4px 22px rgba(0,0,0,.12)}
.card h2{position:absolute;font:700 40px "Lato",sans-serif;color:var(--ink);letter-spacing:.5px}
.card p{position:absolute;font-size:15.5px;line-height:33px;color:#555}
.price{position:absolute;width:134px;height:134px;border-radius:50%;background:var(--navy);border:6px solid #cfd8e2;color:var(--white);text-align:center;font:400 16px/20px "Lato",sans-serif;padding-top:30px}
.price b{display:block;font:700 23px "Lato",sans-serif;margin-top:6px}
/* cta band */
.cta{left:0;top:2362px;width:1200px;height:438px;background:linear-gradient(180deg,#1ea8e0,#1796d2)}
.cta h2{position:absolute;left:0;top:2432px;width:1200px;text-align:center;color:var(--white);font:700 38px/60px "Lato",sans-serif}
.cta-text{left:160px;top:2578px;width:880px;text-align:center;color:var(--white);font-size:14.5px;line-height:32px}
/* demanding */
.dem-frame{left:93px;top:2926px;width:429px;height:529px;background:var(--navy)}
.dem-photo{left:111px;top:2926px;width:429px;height:511px;background:linear-gradient(135deg,#b9a58c,#d9d2c7 45%,#8d9aa6)}
.dem-title{left:594px;top:2920px;font:700 40px/59px "Lato",sans-serif;color:var(--ink)}
.dem-text{left:596px;top:3124px;width:500px;font-size:14px;line-height:30px;color:#555}
.ticks{left:596px;top:3241px;list-style:none;font-size:14px;line-height:30px;color:#444}
.ticks li{display:flex;align-items:center;gap:12px}
.ticks svg{width:13px;height:13px}
/* where */
.where-map{left:460px;top:3569px;width:740px;height:496px;background:linear-gradient(135deg,#ececec,#e2e4e2 60%,#d9e9cf)}
.where-blue{left:0;top:3569px}
.where h2{position:absolute;left:110px;top:3645px;font:700 38px "Lato",sans-serif;color:var(--white)}
.icon-ring{position:absolute;width:54px;height:54px;border-radius:50%;border:2px solid var(--white);display:flex;align-items:center;justify-content:center}
.icon-ring svg{width:22px;height:22px;fill:var(--white)}
.addr{left:186px;top:3731px;color:var(--white);font-size:15px;line-height:28.5px}
.where-dot{left:471px;top:3738px;width:110px;height:110px;border-radius:50%;background:var(--blue);border:7px solid var(--white);box-shadow:0 0 0 6px rgba(27,163,221,.35)}
/* footer */
.footer{left:0;top:4065px;width:1200px;height:446px;background:linear-gradient(180deg,#fafafa,#eeeeee)}
.fcol{position:absolute;top:4160px}
.fcol h3{font:700 20px "Lato",sans-serif;color:#222;margin-bottom:14px}
.fcol ul{list-style:none;font-size:14px;line-height:28.3px;color:#666}
.fline{left:110px;top:4397px;width:978px;height:1px;background:#d6d6d6}
.copy{left:110px;top:4440px;font-size:14px;color:#666}
.legal{right:112px;top:4440px;font-size:14px;color:#666}
</style>
</head>
<body>

<!-- header -->
<div class="abs brand"><span class="mark"></span>NORVEXA</div>
<div class="abs toplinks">
  <span><svg viewBox="0 0 16 12"><path d="M0 0h16v12H0z M0 0l8 6 8-6" /></svg>Contact Us</span><span class="sep">|</span>
  <span><svg viewBox="0 0 16 16"><path d="M3 1l3 0 1 4-2 1.5a9 9 0 0 0 4.5 4.5L11 9l4 1v3a2 2 0 0 1-2 2A13 13 0 0 1 1 3a2 2 0 0 1 2-2z"/></svg>0300 555 014</span><span class="sep">|</span>
  <span><svg viewBox="0 0 14 16"><path d="M2 7V5a5 5 0 0 1 10 0v2h1v9H1V7zm2 0h6V5a3 3 0 0 0-6 0z"/></svg>Login</span>
</div>
<div class="abs trial-top">FREE TRIAL</div>
<nav class="abs nav"><span>COMPANY DATA</span><span>LOCATION DATA</span><span>SERVICES</span><span>ABOUT US</span></nav>

<!-- hero -->
<div class="abs hero" role="img" aria-label="Dark blue background with a glowing network of connected data points"></div>
<div class="abs hero-panel"></div>
<svg class="abs hero-split" width="1200" height="529" viewBox="0 0 1200 529"><path d="M633 0 L571 529" stroke="#fff" stroke-width="5"/></svg>
<div class="abs hero-title" style="left:150px;top:282px">Comprehensive<br>Company Information</div>
<div class="btn light" style="left:150px;top:391px;width:155px;height:48px">COMPANY API</div>
<div class="abs hero-title" style="left:725px;top:282px">Bring Mapping Data Into<br>Your Business</div>
<div class="btn light" style="left:726px;top:391px;width:155px;height:48px">LOCATION API</div>
<div class="abs hero-circle">Richer Data<br>to Drive Your<br>Business</div>

<!-- intro -->
<div class="abs intro">
  <p>Norvexa is setup for connected world. A world where data is integrated, comprehensive and useful. Where systems are designed to cooperate to make businesses more efficient. For this purpose we have focused on two key areas of work - location and company data.</p>
  <p>Our Postcode API, is the most current in the marketplace, helping anyone pinpoint a map simply by providing a postcode. This allows you to assign a location to your postcode-level business data. We also provide an Address API, giving you an address for any postcode along with it's coordinate on the ground. We also supply base maps for customers looking to use maps on their websites. And we supply a wide range of bespoke GIS services, for more specific mapping work.</p>
  <p>For company data we have restructured the national company register data into something more useful and practical for businesses. Just supply one or more company numbers and we can send you back detailed company information covering a raft of data. Better still this data can be supplied either as a file or by API so you can receive it in the format you prefer.</p>
</div>

<!-- company api -->
<svg class="photo" style="left:0;top:1265px" width="823" height="445" viewBox="0 0 823 445" role="img" aria-label="Photo of two business professionals studying a line chart on a large screen">
  <defs><linearGradient id="gCo" x1="0" x2="1"><stop offset="0" stop-color="#7e8fa0"/><stop offset=".55" stop-color="#aab9cc"/><stop offset="1" stop-color="#c9d3e6"/></linearGradient></defs>
  <path d="M0 0H756L823 445H0z" fill="url(#gCo)"/>
</svg>
<div class="card" style="left:652px;top:1309px;width:436px;height:359px">
  <h2 style="left:76px;top:52px">COMPANY API</h2>
  <p style="left:76px;top:118px;width:300px">You supply one or more company numbers - We send back everything via a simple API or CSV file.</p>
  <div class="btn" style="left:76px;top:253px;width:152px;height:46px">FIND OUT MORE</div>
  <div class="btn" style="left:240px;top:253px;width:152px;height:46px">FREE TRIAL</div>
</div>
<div class="price" style="left:581px;top:1427px">FROM<br>ONLY<b>£29 PM</b></div>

<!-- location api -->
<svg class="photo" style="left:377px;top:1789px" width="823" height="445" viewBox="0 0 823 445" role="img" aria-label="Photo of hands using a laptop showing a street map with location pins">
  <defs><linearGradient id="gLo" x1="0" x2="1"><stop offset="0" stop-color="#3a3d42"/><stop offset=".5" stop-color="#c8c9c2"/><stop offset="1" stop-color="#e8d9d0"/></linearGradient></defs>
  <path d="M67 0H823V445H0z" fill="url(#gLo)"/>
</svg>
<div class="card" style="left:110px;top:1833px;width:438px;height:357px">
  <h2 style="left:42px;top:50px">LOCATION API</h2>
  <p style="left:42px;top:116px;width:330px">You send us a postcode we send you the location. Or you send us the location, we send back the postcode: API or CSV.</p>
  <div class="btn" style="left:42px;top:252px;width:152px;height:46px">FIND OUT MORE</div>
  <div class="btn" style="left:206px;top:252px;width:152px;height:46px">FREE TRIAL</div>
</div>
<div class="price" style="left:481px;top:1951px">FROM<br>ONLY<b>£29 PM</b></div>

<!-- cta -->
<div class="abs cta"></div>
<div class="cta"><h2>GO AHEAD: TEST OUR DATA; OR<br>LET'S TALK IT THROUGH...</h2></div>
<div class="abs cta-text">If you are confident you know what you want, why not start a trial? It's free of charge and you can test the service for a limited time, If you are not so sure or you have a very specific requirements then talk to our consultants.</div>
<div class="btn light" style="left:443px;top:2675px;width:151px;height:44px">FIND OUT MORE</div>
<div class="btn light" style="left:606px;top:2675px;width:150px;height:44px">FREE TRIAL</div>

<!-- demanding data -->
<div class="abs dem-frame"></div>
<div class="abs dem-photo" role="img" aria-label="Photo of a team meeting around a table with charts shown on a wall screen"></div>
<div class="abs dem-title">DEMANDING DATA<br>REQUIREMENTS? LOOK NO<br>FURTHER</div>
<div class="abs dem-text">Most businesses looking for our help have complex data requirements they need to piece together. It may be they have an in-house team, but if not, we can help with:</div>
<ul class="abs ticks">
  <li><svg viewBox="0 0 14 14"><circle cx="7" cy="7" r="7" fill="#1ba3dd"/><path d="M3.5 7.2l2.3 2.3 4.7-4.8" stroke="#fff" stroke-width="1.8" fill="none"/></svg>Connecting our API into existing systems and software</li>
  <li><svg viewBox="0 0 14 14"><circle cx="7" cy="7" r="7" fill="#1ba3dd"/><path d="M3.5 7.2l2.3 2.3 4.7-4.8" stroke="#fff" stroke-width="1.8" fill="none"/></svg>Helping with more complex business or location data supply</li>
  <li><svg viewBox="0 0 14 14"><circle cx="7" cy="7" r="7" fill="#1ba3dd"/><path d="M3.5 7.2l2.3 2.3 4.7-4.8" stroke="#fff" stroke-width="1.8" fill="none"/></svg>Placing experienced staff on site to assist with mapping and data projects</li>
  <li><svg viewBox="0 0 14 14"><circle cx="7" cy="7" r="7" fill="#1ba3dd"/><path d="M3.5 7.2l2.3 2.3 4.7-4.8" stroke="#fff" stroke-width="1.8" fill="none"/></svg>Helping businesses automate and digitally transform</li>
</ul>
<div class="btn" style="left:597px;top:3395px;width:176px;height:44px">BESPOKE SERVICES</div>

<!-- where -->
<div class="abs where-map" role="img" aria-label="Street map of the area around the office with nearby business locations"></div>
<svg class="abs where-blue" width="600" height="496" viewBox="0 0 600 496">
  <defs><linearGradient id="gWh" x1="0" y1="0" x2="0" y2="1"><stop offset="0" stop-color="#1a9ad8"/><stop offset="1" stop-color="#16478a"/></linearGradient></defs>
  <path d="M0 0H508L573 496H0z" fill="url(#gWh)"/>
</svg>
<div class="where"><h2>WHERE IS NORVEXA?</h2></div>
<div class="icon-ring" style="left:111px;top:3726px"><svg viewBox="0 0 24 24"><path d="M12 2a7 7 0 0 0-7 7c0 5 7 13 7 13s7-8 7-13a7 7 0 0 0-7-7zm0 9.5A2.5 2.5 0 1 1 12 6.5a2.5 2.5 0 0 1 0 5z"/></svg></div>
<div class="abs addr">Second Floor, 8 Halden Court<br>Brookmere Park<br>Thornbury<br>Ashford TN9 4QX</div>
<div class="icon-ring" style="left:111px;top:3857px"><svg viewBox="0 0 16 16"><path d="M3 1l3 0 1 4-2 1.5a9 9 0 0 0 4.5 4.5L11 9l4 1v3a2 2 0 0 1-2 2A13 13 0 0 1 1 3a2 2 0 0 1 2-2z"/></svg></div>
<div class="abs addr" style="top:3870px">Contact: 0300 555 014</div>
<div class="btn light" style="left:110px;top:3956px;width:162px;height:44px">SEND AN EMAIL</div>
<div class="abs where-dot"></div>

<!-- footer -->
<div class="abs footer" role="img" aria-label="Faint city skyline in light grey"></div>
<div class="fcol" style="left:110px"><h3>COMPANY DATA</h3><ul><li>Company Information</li><li>Alerts and Notifications</li><li>Contact Information</li><li>Financial Information</li><li>Other Data Services</li></ul></div>
<div class="fcol" style="left:368px"><h3>LOCATION DATA</h3><ul><li>Postcode Lookup</li><li>Address Lookup</li><li>Base Mapping</li><li>Boundaries</li><li>Bespoke Mapping</li></ul></div>
<div class="fcol" style="left:625px"><h3>SERVICES</h3><ul><li>API / Integrations</li><li>Licensing / IPR</li><li>Complex Location Data</li><li>Digital Transformation</li></ul></div>
<div class="fcol" style="left:883px"><h3>NORVEXA</h3><ul><li>Pricing</li><li>About Us</li><li>Contact Us</li><li>Free Trial</li><li>Login</li></ul></div>
<div class="abs fline"></div>
<div class="abs copy">Norvexa © 2019 All rights reserved.</div>
<div class="abs legal">Sitemap &nbsp;|&nbsp; Terms &amp;of Use &nbsp;|&nbsp; Privacy Policy &nbsp;|&nbsp; Contact us</div>

</body>
</html>
```